Luxury Face Oil Label

I'm looking for a simple and sophisticated design for a natural face oil that will target the luxe market. It is a pure Natural product. I have attached the logo, Velumi Organics.

Here's the Copy

LUXE FACIAL OIL

Regenerate. Hydrate. Glow

100% Natural

30ml (1.01 oz)

A complex blend of Pure Oils including Marula, Sea Buckthorn, Rosehip, Neroli, Evening primrose, Argan, Calendula, Lavender, Jojoba, Grapeseed, Baobab, Moringa and Vitamin E oil.

Produced by
Brasso Kettle Ltd
P.O box 7925-00300
Nairobi, Kenya
www.velumiorganics.example

Target Market(s)

High end

Requirements
Must have
• Simple, Please consider the bottle, which is a 30ml clear glass bottle with a gold and white pump. Image attached.
Nice to have
• Very clean designs, not too much going on.
Should not have
• Leaves and nuts.

```html
<!DOCTYPE html>
<html lang="en">
<head>
<meta charset="utf-8">
<title>Velumi Organics – Luxe Facial Oil Label</title>
<link href="https://fonts.googleapis.com/css2?family=Jost:wght@400;500&family=Tenor+Sans&display=swap" rel="stylesheet">
<style>
  :root {
    --backdrop: #f4f5f5;
    --label: #ffffff;
    --ink: #1e1e1e;
    --ink-soft: #3a3a3a;
    --sage: #b8ba9a;
    --sage-ink: #8d8f6c;
    --rule: #4a4a4a;
  }
  html, body {
    margin: 0;
    padding: 0;
    width: 1200px;
    height: 900px;
    overflow: hidden;
    background: var(--backdrop);
  }
  .canvas {
    position: relative;
    width: 1200px;
    height: 900px;
  }
  .label {
    position: absolute;
    left: 199px;
    top: 290px;
    width: 802px;
    height: 321px;
    background: var(--label);
    font-family: "Jost", sans-serif;
    color: var(--ink);
  }
  .ingredients {
    position: absolute;
    left: 40px;
    top: 72px;
    width: 200px;
    margin: 0;
    text-align: center;
    font-size: 11px;
    line-height: 23px;
    letter-spacing: 0.4px;
    color: var(--ink-soft);
  }
  .front {
    position: absolute;
    left: 250px;
    top: 0;
    width: 300px;
    text-align: center;
  }
  .brand {
    margin-top: 60px;
    display: flex;
    flex-direction: column;
    align-items: center;
    gap: 6px;
  }
  .brand-name {
    font-family: "Tenor Sans", sans-serif;
    font-size: 22px;
    letter-spacing: 4px;
    color: var(--sage-ink);
    text-transform: uppercase;
  }
  .product-name {
    margin: 56px 0 0;
    font-family: "Tenor Sans", sans-serif;
    font-weight: 400;
    font-size: 19px;
    letter-spacing: 3.5px;
    color: var(--ink);
  }
  .benefits {
    margin: 8px 0 0;
    font-size: 8px;
    letter-spacing: 2px;
    font-weight: 500;
  }
  .divider {
    width: 215px;
    height: 0;
    border: 0;
    border-top: 1px solid var(--rule);
    margin: 24px auto 0;
  }
  .claim {
    margin: 13px 0 0;
    font-size: 9px;
    letter-spacing: 1.8px;
    font-weight: 500;
  }
  .producer {
    position: absolute;
    left: 560px;
    top: 86px;
    width: 200px;
    margin: 0;
    text-align: center;
    font-style: normal;
    font-size: 10px;
    line-height: 22.5px;
    letter-spacing: 0.5px;
    color: var(--ink-soft);
  }
  .producer strong {
    font-weight: 500;
    color: var(--ink);
  }
  .volume-band {
    position: absolute;
    left: 0;
    bottom: 0;
    width: 100%;
    height: 40px;
    background: var(--sage);
    display: flex;
    align-items: center;
    justify-content: center;
    font-size: 8px;
    letter-spacing: 1.5px;
    color: #ffffff;
  }
</style>
</head>
<body>
<main class="canvas">
  <section class="label">
    <p class="ingredients">A complex blend of Pure Oils including Marula, Sea Buckthorn, Rosehip, Neroli, Evening primrose, Argan, Calendula, Lavender, Jojoba, Grapeseed, Baobab, Moringa and Vitamin E oil.</p>

    <div class="front">
      <div class="brand">
        <span class="brand-name">Velumi Organics</span>
      </div>
      <h1 class="product-name">LUXE FACIAL OIL</h1>
      <p class="benefits">REGENERATE • HYDRATE • GLOW</p>
      <hr class="divider">
      <p class="claim">100% NATURAL</p>
    </div>

    <address class="producer">
      <strong>Produced By :</strong><br>
      Brasso Kettle Ltd<br>
      P.O Box 7925-00300<br>
      Nairobi, Kenya<br>
      www.velumiorganics.example
    </address>

    <div class="volume-band">30ml (1.01 oz)</div>
  </section>
</main>
</body>
</html>
```